Business card design for new, innovative company - BoldHarbor

We are a new company looking for a business card design that is fun, different and quirky. Must use corporate colour green - CMYK C:55, M:0, Y:100, K:0, and corporate colour grey - C:0, M:0, Y: 0, K:70.

We have developed the first real time data application, in which people are able to profile the data of their existing customers in order to pull out more good fit clients to direct their marketing activities at.

Industry/Entity Type

Marketing

Requirements
Must have
• Logo, name, title, telephone number, fax number, email, website, address

```html
<!DOCTYPE html>
<html lang="en">
<head>
<meta charset="utf-8">
<title>BoldHarbor Business Card</title>
<link rel="stylesheet" href="https://fonts.googleapis.com/css2?family=Mulish:wght@400;800&display=swap">
<style>
  :root {
    --brand-green: #84c225;
    --brand-grey: #4d4d4f;
    --card-dark: #5e6062;
    --card-dark-deep: #4a4c4e;
    --card-white: #ffffff;
    --backdrop: #ecebe8;
    --text-grey: #4d4d4f;
  }
  * { box-sizing: border-box; margin: 0; padding: 0; }
  html, body {
    width: 1200px; height: 1000px; overflow: hidden;
    background: var(--backdrop);
    font-family: "Mulish", Arial, sans-serif;
  }
  .canvas { position: relative; width: 1200px; height: 1000px; }

  .card {
    position: absolute;
    width: 760px; height: 430px;
    border-radius: 34px;
    overflow: hidden;
    box-shadow: 0 6px 18px rgba(0,0,0,0.18);
  }

  /* Back of card */
  .card-back { left: 70px; top: 50px; background: var(--card-dark); }
  .card-back .pattern-area {
    position: absolute; inset: 0;
    background: radial-gradient(ellipse at 55% 45%, var(--card-dark) 0%, var(--card-dark-deep) 100%);
  }
  .card-back .brand {
    position: absolute; left: 150px; top: 210px;
    display: flex; align-items: center; gap: 16px;
  }
  .card-back .brand-name {
    font-weight: 800; font-size: 74px; letter-spacing: -2px;
    color: var(--brand-green); line-height: 1;
  }
  .brand-square {
    width: 30px; height: 30px; border-radius: 6px;
    background: var(--brand-green);
  }

  /* Front of card */
  .card-front { left: 370px; top: 520px; background: var(--card-white); }
  .card-front .brand {
    position: absolute; left: 60px; top: 58px;
    display: flex; align-items: center; gap: 12px;
  }
  .card-front .brand-name {
    font-weight: 800; font-size: 54px; letter-spacing: -1.5px;
    color: var(--brand-grey); line-height: 1;
  }
  .card-front .brand-square { width: 22px; height: 22px; border-radius: 5px; background: var(--brand-grey); }

  .address {
    position: absolute; left: 60px; top: 238px;
    color: var(--text-grey); font-size: 18px; line-height: 1.25;
  }
  .address-label {
    color: var(--brand-green); font-weight: 800; font-size: 24px;
    margin-bottom: 14px;
  }

  .contact {
    position: absolute; right: 44px; top: 272px;
    text-align: right; color: var(--text-grey);
  }
  .contact-name {
    color: var(--brand-green); font-weight: 800; font-size: 26px;
    margin-bottom: 12px; margin-right: 24px;
  }
  .contact-list { list-style: none; font-size: 17px; line-height: 1.35; }
  .contact-list li { display: flex; justify-content: flex-end; align-items: center; gap: 8px; }
  .contact-icon {
    display: inline-block; width: 14px; height: 14px;
    border: 1.5px solid var(--brand-grey); border-radius: 3px;
    background: #f3f3f3;
  }
</style>
</head>
<body>
<main class="canvas">

  <section class="card card-back" aria-label="Card back">
    <div class="pattern-area" role="img" aria-label="Grid of soft embossed rounded squares in dark grey"></div>
    <div class="brand">
      <span class="brand-name">BoldHarbor</span>
      <span class="brand-square"></span>
    </div>
  </section>

  <section class="card card-front" aria-label="Card front">
    <div class="brand">
      <span class="brand-name">BoldHarbor</span>
      <span class="brand-square"></span>
    </div>

    <address class="address" style="font-style: normal;">
      <div class="address-label">Address</div>
      22 Millbrook Lane,<br>
      Ely,<br>
      Cambridgeshire,<br>
      CB7 4QT
    </address>

    <div class="contact">
      <div class="contact-name">Jenna Collins</div>
      <ul class="contact-list">
        <li>07831 552904 <span class="contact-icon"></span></li>
        <li>01223 480917 <span class="contact-icon"></span></li>
        <li>jenna.collins@boldharbor.com <span class="contact-icon"></span></li>
        <li>www.boldharbor.com <span class="contact-icon"></span></li>
      </ul>
    </div>
  </section>

</main>
</body>
</html>
```